New App: 4 Page Design - Updated Brief

We need an indicative design for our new app 'Kit Runner', a delivery service for tools and hardware in Sydney, Australia.

Imagine a service which copies the blue print of Parcel Pantry, but for tools and Hardware. Where builders and tradespeople are stuck on-site at work and need a tool to be delivered to them on-site, same day. They can jump onto this app and in-put their address, then select an item from the catalogue and confirm the order. Once the order has been collected and due for delivery a map will show the location of the delivery driver.

We'd like 4 pages designed.

1st page) Loading page, similar to but not the same as the ParcelPantry example attached.

2nd page) Home page - featuring the logo and some icons which direct users around the website. (Please see link to design example: https://www.parcelpantry.example/au?ref_id=ab12c3d4-e5f6-47a8-91b2-c3d4e5f6a7b8 )

3rd page) A page which depicts the catalogue of tools and hardware (showing generic tools available (Please see link to design example https://www.toolvault.example/products/building-hardware).

4th page) We'd like a page which shows a map, tracking the delivery, from the hardware store, to the location of the purchaser, exactly like any typical zipto delivery service.

Please see the below website for design guidance and ideas

https://www.toolvault.example/?src=ad.xy&ref=Qw7RtYuIoPaSdFgHjKlZxCvBnM2q9w8e7r6t5y4u3i2o1pLkJhGfDsAzXcVbNmQwErTyUiOp_abC

Target Market(s)

Construction industry, tradespeople

Industry/Entity Type

Construction and Tradesmen

Colors

Designer to choose colors to be used in the design.

Requirements
Must have
• Desired Colour schemes: up to the designer but no bright colours
Nice to have
• An icon bar at the bottom of the page that directs you to the various pages on the app. Example shown in the attachments
Should not have
• An exact copy of the Zipto App

```html
<!DOCTYPE html>
<html lang="en">
<head>
<meta charset="utf-8">
<title>Kit Runner – App Screens</title>
<link href="https://fonts.googleapis.com/css2?family=Inter:wght@400;500;600;700&display=swap" rel="stylesheet">
<style>
  :root{
    --yellow:#f6c400;
    --yellow-soft:#fcdc45;
    --ink:#111111;
    --muted:#6e6e6e;
    --screen:#f6f6f6;
    --card:#ffffff;
    --field:#ebebeb;
    --frame:#111111;
  }
  *{box-sizing:border-box;margin:0;padding:0}
  html,body{width:1136px;height:1200px;overflow:hidden;background:#fff;font-family:"Inter",sans-serif;color:var(--ink)}
  .board{position:absolute;left:0;top:0;width:1876px;height:1988px;transform:scale(0.6035);transform-origin:0 0}
  .slot{position:absolute}
  .slot.small{transform:scale(0.9);transform-origin:0 0}

  .phone{position:relative;width:316px;border:5px solid var(--frame);border-radius:24px;overflow:hidden;background:var(--screen)}
  .phone.splash{background:#fff}
  .abs{position:absolute}
  svg.ic{width:20px;height:20px;fill:none;stroke:currentColor;stroke-width:1.8;stroke-linecap:round;stroke-linejoin:round}

  .status{position:absolute;left:13px;top:9px;right:13px;height:18px;display:flex;justify-content:space-between;align-items:center;font-size:13px;font-weight:600}
  .status svg{width:52px;height:12px}

  .brand{font-weight:700;color:var(--yellow);letter-spacing:.3px}

  /* splash */
  .splash-mark{position:absolute;left:0;right:0;top:330px;text-align:center;font-size:23px}

  /* header */
  .title{position:absolute;left:45px;top:50px;font-size:18px;font-weight:600}
  .back{position:absolute;left:17px;top:52px;width:18px;height:18px}
  .cart-top{position:absolute;left:236px;top:48px;width:24px;height:24px}
  .kebab{position:absolute;left:277px;top:50px;width:20px;height:20px}
  .badge{position:absolute;width:12px;height:12px;border-radius:50%;background:var(--yellow);color:var(--ink);font-size:8px;font-weight:700;display:flex;align-items:center;justify-content:center}

  /* home */
  .menu{position:absolute;left:18px;top:52px;width:20px;height:20px;color:var(--yellow)}
  .home .brand{position:absolute;left:55px;top:44px;font-size:24px}
  .avatar{position:absolute;border-radius:50%;background:linear-gradient(135deg,#b8c2cc,#4d5b68)}
  .card{position:absolute;background:var(--card);border-radius:8px}
  .card-head{position:absolute;left:13px;right:13px;top:12px;display:flex;justify-content:space-between;align-items:baseline}
  .card-head h3,.section h3{font-size:15px;font-weight:600}
  .see-all{font-size:11px;color:var(--yellow)}
  .cat-row{position:absolute;left:9px;top:45px;display:flex;gap:12px}
  .cat{width:56px;text-align:center;font-size:9.5px;line-height:1.25;color:#333}
  .cat .thumb{width:54px;height:54px;border-radius:10px;margin:0 auto 5px}

  .hero{position:absolute;left:19px;top:278px;width:276px;height:250px;border-radius:8px;background:linear-gradient(150deg,var(--yellow-soft),var(--yellow) 70%)}
  .hero h2{position:absolute;left:19px;top:15px;width:230px;color:#fff;font-size:17px;font-weight:600;line-height:1.2}
  .field{position:absolute;left:19px;width:240px;height:43px;background:#fff;border-radius:4px;display:flex;align-items:center;padding:0 12px;gap:12px;font-size:12px;color:var(--muted)}
  .field svg{width:14px;height:14px}
  .field .ic-fill{fill:var(--ink);stroke:none}
  .field .grow{flex:1;color:var(--ink)}
  .field .placeholder{flex:1}
  .btn{position:absolute;left:19px;top:190px;width:240px;height:43px;background:var(--ink);color:#fff;border-radius:4px;font-size:14px;font-weight:600;display:flex;align-items:center;justify-content:center}

  .section{position:absolute;left:15px;right:15px;display:flex;justify-content:space-between;align-items:baseline}
  .section h3{font-size:16px}
  .rail{position:absolute;left:12px;display:flex;gap:9px}
  .product{width:97px;font-size:11px;line-height:1.2;color:#333}
  .product .thumb{height:104px;background:#fff;border-radius:4px;margin-bottom:13px;position:relative;overflow:hidden}
  .product .thumb i{position:absolute;left:12px;right:12px;top:10px;bottom:10px;border-radius:4px}
  .product .name{height:28px;overflow:hidden;white-space:nowrap}
  .product .name span{display:block;overflow:hidden;text-overflow:clip}
  .price-row{display:flex;justify-content:space-between;align-items:center;margin-top:6px}
  .price{color:var(--yellow);font-weight:600;font-size:13px}
  .rate{font-size:8.5px;color:#444}
  .rate b{color:var(--yellow);font-weight:400}
  .shop{width:97px;font-size:11px;color:#333}
  .shop .thumb{height:67px;border-radius:4px;margin-bottom:9px}
  .shop .km{font-size:9.5px;color:var(--muted);margin-top:3px;display:flex;align-items:center;gap:2px}
  .shop .km svg{width:9px;height:9px;fill:var(--yellow);stroke:none}

  /* tab bar */
  .tabbar{position:absolute;left:0;right:0;bottom:4px;height:54px;padding-left:10px;display:grid;grid-template-columns:repeat(4,73px);background:var(--screen)}
  .tab{display:flex;flex-direction:column;align-items:center;gap:3px;font-size:9.5px;color:#555;position:relative;padding-top:6px}
  .tab svg{width:21px;height:21px}
  .tab.active{color:var(--yellow)}
  .tab .badge{left:40px;top:3px}

  /* categories */
  .search{position:absolute;left:20px;top:92px;width:276px;height:42px;background:var(--field);border-radius:6px;display:flex;align-items:center;gap:8px;padding:0 12px;font-size:12px;color:var(--muted)}
  .search svg{width:16px;height:16px}
  .search span{flex:1}
  .label-h{position:absolute;left:22px;font-size:15px;font-weight:600}
  .featured{position:absolute;left:20px;top:195px;display:flex;gap:10px;width:320px}
  .feat{width:96px;font-size:10px;line-height:1.2;color:#333;white-space:nowrap}
  .feat .thumb{height:65px;border-radius:4px;margin-bottom:6px}
  .tile{position:absolute;width:132px;background:var(--card);border-radius:6px;overflow:hidden;box-shadow:0 1px 3px rgba(0,0,0,.06)}
  .tile .thumb{width:100%}
  .tile p{text-align:center;font-size:11.5px;font-weight:500;line-height:1.2;padding:8px 4px}

  /* tracking */
  .eta{position:absolute;left:17px;top:90px;font-size:22px;font-weight:600}
  .eta-sub{position:absolute;left:17px;top:124px;font-size:13px;color:#444}
  .eta-sub b{color:var(--ink);font-weight:600}
  .map{position:absolute;left:15px;top:158px;width:276px;height:420px;border-radius:6px;background:linear-gradient(160deg,#e9e9e9,#dcdcdc 60%,#d6dfd3)}
  .plate{position:absolute;left:152px;top:190px;width:117px;height:48px;background:#1a1a1a;border-radius:4px;color:#fff;display:flex;align-items:center;gap:8px;padding:0 8px}
  .plate .dot{width:32px;height:32px;border-radius:50%;background:#fff}
  .plate small{display:block;font-size:8px;color:#ccc}
  .plate strong{font-size:12px;font-weight:600}
  .driver{position:absolute;left:25px;top:533px;width:257px;height:67px;background:#fff;border-radius:6px;box-shadow:0 2px 8px rgba(0,0,0,.08)}
  .driver .who{position:absolute;left:58px;top:12px;font-size:10px;color:var(--muted);line-height:1.3}
  .driver .who strong{display:block;font-size:13px;color:var(--ink);font-weight:600}
  .driver .who em{font-style:normal;font-size:8px}
  .driver .who em b{color:var(--yellow);font-weight:400}
  .profile-link{position:absolute;right:10px;top:26px;font-size:11px;color:var(--yellow);display:flex;align-items:center;gap:4px}
  .profile-link svg{width:12px;height:12px}
  .message{position:absolute;left:15px;top:625px;width:235px;height:42px;background:var(--field);border-radius:6px;display:flex;align-items:center;padding:0 12px;font-size:12px;color:#444}
  .message span{flex:1}
  .message svg{width:16px;height:16px}
  .call{position:absolute;left:258px;top:625px;width:34px;height:42px;background:var(--field);border-radius:6px;display:flex;align-items:center;justify-content:center}
  .call svg{width:16px;height:16px;fill:var(--ink);stroke:none}

  .signature{position:absolute;left:1535px;top:1852px;font-size:50px}

  /* placeholder fills */
  .g-wall{background:linear-gradient(160deg,#c9ccd0,#8a8f95)}
  .g-fast{background:linear-gradient(150deg,#6c7480,#2f3540)}
  .g-concrete{background:linear-gradient(160deg,#b9b2a6,#7f7a71)}
  .g-door{background:linear-gradient(160deg,#f1f1f1,#bdbdbd)}
  .g-steel{background:linear-gradient(160deg,#c2ccd8,#7d8b9b)}
  .g-fence{background:linear-gradient(160deg,#9fc4d6,#6c8f5c)}
  .g-build{background:linear-gradient(160deg,#d9b48c,#4a3f36)}
  .g-timber{background:linear-gradient(160deg,#3a3330,#c48e52)}
  .g-tools{background:linear-gradient(150deg,#d7c26a,#6c6f74)}
  .g-vac{background:linear-gradient(160deg,#d2d2d2,#8c7b7e)}
  .g-shelf{background:linear-gradient(160deg,#9aa0a6,#5e5448)}
  .g-paint{background:linear-gradient(160deg,#3f4a5a,#c9ccd0)}
  .g-drill{background:linear-gradient(160deg,#e8ecef,#2e8a94)}
  .g-rack{background:linear-gradient(160deg,#f2f2f2,#b5b5b5)}
  .g-store{background:linear-gradient(150deg,#c8c06a,#4d5348)}
</style>
</head>
<body>
<svg width="0" height="0" style="position:absolute" aria-hidden="true">
  <defs>
    <symbol id="i-status" viewBox="0 0 52 12"><rect x="0" y="8" width="3" height="4" fill="#111"/><rect x="4.5" y="6" width="3" height="6" fill="#111"/><rect x="9" y="3.5" width="3" height="8.5" fill="#111"/><rect x="13.5" y="1" width="3" height="11" fill="#111"/><path d="M21 4.5a8 8 0 0 1 11 0M23 7a5 5 0 0 1 7 0M25.2 9.4a1.8 1.8 0 0 1 2.6 0" fill="none" stroke="#111" stroke-width="1.6" stroke-linecap="round"/><rect x="36" y="1.5" width="14" height="9" rx="2" fill="#111"/><rect x="50.6" y="4" width="1.4" height="4" fill="#111"/></symbol>
    <symbol id="i-home" viewBox="0 0 24 24"><path d="M4 11l8-7 8 7v9h-5v-6H9v6H4z"/></symbol>
    <symbol id="i-search" viewBox="0 0 24 24"><circle cx="11" cy="11" r="6.5"/><path d="M16 16l4.5 4.5"/></symbol>
    <symbol id="i-cart" viewBox="0 0 24 24"><path d="M2.5 4h3l2.3 11h10.4l2.3-8H7"/><circle cx="9" cy="19.5" r="1.3"/><circle cx="17" cy="19.5" r="1.3"/></symbol>
    <symbol id="i-gear" viewBox="0 0 24 24"><path d="M12 3l8 4.5v9L12 21l-8-4.5v-9z"/><circle cx="12" cy="12" r="3"/></symbol>
    <symbol id="i-menu" viewBox="0 0 24 24"><path d="M5 7h14M5 12h14M5 17h14"/></symbol>
    <symbol id="i-kebab" viewBox="0 0 24 24"><circle cx="12" cy="5" r="1.6" fill="currentColor"/><circle cx="12" cy="12" r="1.6" fill="currentColor"/><circle cx="12" cy="19" r="1.6" fill="currentColor"/></symbol>
    <symbol id="i-left" viewBox="0 0 24 24"><path d="M15 5l-7 7 7 7"/></symbol>
    <symbol id="i-right" viewBox="0 0 24 24"><path d="M9 5l7 7-7 7"/></symbol>
    <symbol id="i-down" viewBox="0 0 24 24"><path d="M5 9l7 7 7-7"/></symbol>
    <symbol id="i-mic" viewBox="0 0 24 24"><rect x="9" y="3" width="6" height="11" rx="3"/><path d="M6 11a6 6 0 0 0 12 0M12 17v4"/></symbol>
    <symbol id="i-pin" viewBox="0 0 24 24"><path d="M12 2a7 7 0 0 0-7 7c0 5.2 7 13 7 13s7-7.8 7-13a7 7 0 0 0-7-7z"/><circle cx="12" cy="9" r="2.6" fill="#fff"/></symbol>
    <symbol id="i-clock" viewBox="0 0 24 24"><circle cx="12" cy="12" r="10"/><path d="M12 7v5l3 2" stroke="#fff" stroke-width="2.2" fill="none" stroke-linecap="round"/></symbol>
    <symbol id="i-phone" viewBox="0 0 24 24"><path d="M6.6 3.5l3 .3 1.3 4-2 1.5a12 12 0 0 0 5.8 5.8l1.5-2 4 1.3.3 3c0 1-1 2.1-2.2 2.1C10.6 19.5 4.5 13.4 4.5 5.7c0-1.2 1-2.2 2.1-2.2z"/></symbol>
  </defs>
</svg>

<main class="board">

  <!-- ===== Row 1 ===== -->
  <div class="slot small" style="left:296px;top:85px">
    <section class="phone splash" style="height:691px">
      <p class="splash-mark brand">Kit Runner...</p>
    </section>
  </div>

  <div class="slot small" style="left:630px;top:85px">
    <section class="phone home" style="height:691px">
      <div class="status"><span>9:41</span><svg><use href="#i-status"/></svg></div>
      <svg class="ic menu"><use href="#i-menu"/></svg>
      <span class="brand">Kit Runner</span>
      <div class="avatar" style="left:266px;top:44px;width:30px;height:30px" role="img" aria-label="User profile photo"></div>
      <div class="card" style="left:17px;top:113px;width:280px;height:140px">
        <div class="card-head"><h3>Categories</h3><span class="see-all">See All</span></div>
        <div class="cat-row">
          <div class="cat"><div class="thumb g-wall" role="img" aria-label="General hardware photo"></div>General Hardware</div>
          <div class="cat"><div class="thumb g-fast" role="img" aria-label="Fasteners photo"></div>Fasteners &amp; Fixings</div>
          <div class="cat"><div class="thumb g-concrete" role="img" aria-label="Concrete work photo"></div>Concrete &amp; Cementing</div>
          <div class="cat"><div class="thumb g-door" role="img" aria-label="Door hardware photo"></div>Door Hardware</div>
        </div>
      </div>
      <div class="hero">
        <h2>Find and order tools and hardware</h2>
        <div class="field" style="top:75px"><svg class="ic-fill"><use href="#i-pin"/></svg><span class="placeholder">Enter delivery address</span></div>
        <div class="field" style="top:128px"><svg class="ic-fill"><use href="#i-clock"/></svg><span class="grow">Deliver now</span><svg class="ic" style="color:#111"><use href="#i-down"/></svg></div>
        <div class="btn">Find Tools</div>
      </div>
      <div class="section" style="top:552px"><h3>Products we recommend</h3></div>
      <div class="rail" style="top:588px">
        <div class="product"><div class="thumb"><i class="g-paint" role="img" aria-label="Paint tin product photo"></i></div></div>
        <div class="product"><div class="thumb"><i class="g-drill" role="img" aria-label="Cordless drill kit photo"></i></div></div>
        <div class="product"><div class="thumb"><i class="g-rack" role="img" aria-label="Shelving rack photo"></i></div></div>
      </div>
      <nav class="tabbar">
        <a class="tab active"><svg class="ic"><use href="#i-home"/></svg><span>Home</span></a>
        <a class="tab"><svg class="ic"><use href="#i-search"/></svg><span>Browse</span></a>
        <a class="tab"><svg class="ic"><use href="#i-cart"/></svg><span>Basket</span><i class="badge">1</i></a>
        <a class="tab"><svg class="ic"><use href="#i-gear"/></svg><span>Setting</span></a>
      </nav>
    </section>
  </div>

  <div class="slot small" style="left:963px;top:85px">
    <section class="phone" style="height:691px">
      <div class="status"><span>9:41</span><svg><use href="#i-status"/></svg></div>
      <svg class="ic back"><use href="#i-left"/></svg>
      <h1 class="title">Categories</h1>
      <svg class="ic cart-top"><use href="#i-cart"/></svg><i class="badge" style="left:252px;top:44px">1</i>
      <svg class="ic kebab"><use href="#i-kebab"/></svg>
      <div class="search"><svg class="ic"><use href="#i-search"/></svg><span>Search tools and hardware</span><svg class="ic"><use href="#i-mic"/></svg></div>
      <h2 class="label-h" style="top:157px">Featured categories this week</h2>
      <div class="featured">
        <div class="feat"><div class="thumb g-tools" role="img" aria-label="Power tools collection photo"></div>Tools</div>
        <div class="feat"><div class="thumb g-vac" role="img" aria-label="Vacuum cleaner photo"></div>Vacuum &amp; Steam<br>Cleaners</div>
        <div class="feat"><div class="thumb g-shelf" role="img" aria-label="Storage shelving photo"></div>Storage &amp; Shelving</div>
      </div>
      <h2 class="label-h" style="top:312px">All</h2>
      <div class="tile" style="left:20px;top:350px"><div class="thumb g-wall" style="height:83px" role="img" aria-label="Ladder against wall photo"></div><p>General Hardware</p></div>
      <div class="tile" style="left:20px;top:483px"><div class="thumb g-concrete" style="height:84px" role="img" aria-label="Concrete trowel photo"></div><p>Concrete &amp; Cementing</p></div>
      <div class="tile" style="left:20px;top:617px"><div class="thumb g-steel" style="height:85px" role="img" aria-label="Steel sheeting photo"></div><p>Steel &amp; Aluminium<br>Section</p></div>
      <div class="tile" style="left:163px;top:350px"><div class="thumb g-fast" style="height:173px" role="img" aria-label="Fasteners and fixings photo"></div><p>Fasteners &amp; Fixings</p></div>
      <div class="tile" style="left:163px;top:573px"><div class="thumb g-door" style="height:83px" role="img" aria-label="Sliding door photo"></div><p>Door Hardware</p></div>
      <nav class="tabbar">
        <a class="tab active"><svg class="ic"><use href="#i-home"/></svg><span>Home</span></a>
        <a class="tab"><svg class="ic"><use href="#i-search"/></svg><span>Browse</span></a>
        <a class="tab"><svg class="ic"><use href="#i-cart"/></svg><span>Basket</span><i class="badge">1</i></a>
        <a class="tab"><svg class="ic"><use href="#i-gear"/></svg><span>Setting</span></a>
      </nav>
    </section>
  </div>

  <div class="slot small" style="left:1297px;top:85px">
    <section class="phone" style="height:691px">
      <div class="status"><span>9:41</span><svg><use href="#i-status"/></svg></div>
      <svg class="ic back"><use href="#i-left"/></svg>
      <h1 class="title">Live Tracking</h1>
      <svg class="ic cart-top"><use href="#i-cart"/></svg><i class="badge" style="left:252px;top:44px">1</i>
      <svg class="ic kebab"><use href="#i-kebab"/></svg>
      <p class="eta">In 15 min</p>
      <p class="eta-sub">Estimated arrival time: <b>6.00 pm</b></p>
      <div class="map" role="img" aria-label="Street map with the delivery route from store to site"></div>
      <div class="plate"><span class="dot"></span><span><small>Scooty</small><strong>BAC-XXXX</strong></span></div>
      <div class="driver">
        <div class="avatar" style="left:10px;top:17px;width:36px;height:36px" role="img" aria-label="Driver photo"></div>
        <div class="who">Driver Name<strong>Sam Ortega</strong><em><b>★</b> 4.5</em></div>
        <span class="profile-link">View Profile <svg class="ic"><use href="#i-right"/></svg></span>
      </div>
      <div class="message"><span>Send a message...</span><svg class="ic"><use href="#i-mic"/></svg></div>
      <div class="call"><svg><use href="#i-phone"/></svg></div>
    </section>
  </div>

  <!-- ===== Row 2 ===== -->
  <div class="slot" style="left:224px;top:808px">
    <section class="phone splash" style="height:692px;width:316px">
      <p class="splash-mark brand">Kit Runner...</p>
    </section>
  </div>

  <div class="slot" style="left:595px;top:808px">
    <section class="phone home" style="height:1012px">
      <div class="status"><span>9:41</span><svg><use href="#i-status"/></svg></div>
      <svg class="ic menu"><use href="#i-menu"/></svg>
      <span class="brand">Kit Runner</span>
      <div class="avatar" style="left:266px;top:44px;width:30px;height:30px" role="img" aria-label="User profile photo"></div>
      <div class="card" style="left:17px;top:113px;width:280px;height:140px">
        <div class="card-head"><h3>Categories</h3><span class="see-all">See All</span></div>
        <div class="cat-row">
          <div class="cat"><div class="thumb g-wall" role="img" aria-label="General hardware photo"></div>General Hardware</div>
          <div class="cat"><div class="thumb g-fast" role="img" aria-label="Fasteners photo"></div>Fasteners &amp; Fixings</div>
          <div class="cat"><div class="thumb g-concrete" role="img" aria-label="Concrete work photo"></div>Concrete &amp; Cementing</div>
          <div class="cat"><div class="thumb g-door" role="img" aria-label="Door hardware photo"></div>Door Hardware</div>
        </div>
      </div>
      <div class="hero">
        <h2>Find and order tools and hardware</h2>
        <div class="field" style="top:75px"><svg class="ic-fill"><use href="#i-pin"/></svg><span class="placeholder">Enter delivery address</span></div>
        <div class="field" style="top:128px"><svg class="ic-fill"><use href="#i-clock"/></svg><span class="grow">Deliver now</span><svg class="ic" style="color:#111"><use href="#i-down"/></svg></div>
        <div class="btn">Find Tools</div>
      </div>
      <div class="section" style="top:552px"><h3>Products we recommend</h3></div>
      <div class="rail" style="top:588px">
        <div class="product"><div class="thumb"><i class="g-paint" role="img" aria-label="Paint tin product photo"></i></div><div class="name"><span>Harlan QuickDry 10L</span><span>Heavy Duty Glos...</span></div><div class="price-row"><span class="price">$248.90</span><span class="rate"><b>★</b> 4.5</span></div></div>
        <div class="product"><div class="thumb"><i class="g-drill" role="img" aria-label="Cordless drill kit photo"></i></div><div class="name"><span>Torvik 18V 2</span><span>Piece Brushless...</span></div><div class="price-row"><span class="price">$299</span><span class="rate"><b>★</b> 4.5</span></div></div>
        <div class="product"><div class="thumb"><i class="g-rack" role="img" aria-label="Shelving rack photo"></i></div><div class="name"><span>Stackwell 190</span><span>x 1900 x 540mm</span></div><div class="price-row"><span class="price">$203.47</span><span class="rate"><b>★</b> 4.5</span></div></div>
      </div>
      <div class="section" style="top:776px"><h3>Shops near you</h3><span class="see-all">See All</span></div>
      <div class="rail" style="top:813px">
        <div class="shop"><div class="thumb g-store" role="img" aria-label="Hardware store aisle photo"></div>Lorem Ipsum<div class="km"><svg><use href="#i-pin"/></svg>3 km</div></div>
        <div class="shop"><div class="thumb g-store" role="img" aria-label="Hardware store aisle photo"></div>Lorem Ipsum<div class="km"><svg><use href="#i-pin"/></svg>3 km</div></div>
        <div class="shop"><div class="thumb g-store" role="img" aria-label="Hardware store aisle photo"></div>Lorem Ipsum<div class="km"><svg><use href="#i-pin"/></svg>3 km</div></div>
      </div>
      <nav class="tabbar">
        <a class="tab active"><svg class="ic"><use href="#i-home"/></svg><span>Home</span></a>
        <a class="tab"><svg class="ic"><use href="#i-search"/></svg><span>Browse</span></a>
        <a class="tab"><svg class="ic"><use href="#i-cart"/></svg><span>Basket</span><i class="badge">1</i></a>
        <a class="tab"><svg class="ic"><use href="#i-gear"/></svg><span>Setting</span></a>
      </nav>
    </section>
  </div>

  <div class="slot" style="left:966px;top:808px">
    <section class="phone" style="height:1077px">
      <div class="status"><span>9:41</span><svg><use href="#i-status"/></svg></div>
      <svg class="ic back"><use href="#i-left"/></svg>
      <h1 class="title">Categories</h1>
      <svg class="ic cart-top"><use href="#i-cart"/></svg><i class="badge" style="left:252px;top:44px">1</i>
      <svg class="ic kebab"><use href="#i-kebab"/></svg>
      <div class="search"><svg class="ic"><use href="#i-search"/></svg><span>Search tools and hardware</span><svg class="ic"><use href="#i-mic"/></svg></div>
      <h2 class="label-h" style="top:157px">Featured categories this week</h2>
      <div class="featured">
        <div class="feat"><div class="thumb g-tools" role="img" aria-label="Power tools collection photo"></div>Tools</div>
        <div class="feat"><div class="thumb g-vac" role="img" aria-label="Vacuum cleaner photo"></div>Vacuum &amp; Steam<br>Cleaners</div>
        <div class="feat"><div class="thumb g-shelf" role="img" aria-label="Storage shelving photo"></div>Storage &amp; Shelving</div>
      </div>
      <h2 class="label-h" style="top:312px">All</h2>
      <div class="tile" style="left:20px;top:350px"><div class="thumb g-wall" style="height:83px" role="img" aria-label="Ladder against wall photo"></div><p>General Hardware</p></div>
      <div class="tile" style="left:20px;top:483px"><div class="thumb g-concrete" style="height:84px" role="img" aria-label="Concrete trowel photo"></div><p>Concrete &amp; Cementing</p></div>
      <div class="tile" style="left:20px;top:617px"><div class="thumb g-steel" style="height:85px" role="img" aria-label="Steel sheeting photo"></div><p>Steel &amp; Aluminium<br>Section</p></div>
      <div class="tile" style="left:20px;top:752px"><div class="thumb g-build" style="height:174px" role="img" aria-label="Timber boards and drill photo"></div><p>Building Materials &amp;<br>Supplies</p></div>
      <div class="tile" style="left:163px;top:350px"><div class="thumb g-fast" style="height:173px" role="img" aria-label="Fasteners and fixings photo"></div><p>Fasteners &amp; Fixings</p></div>
      <div class="tile" style="left:163px;top:573px"><div class="thumb g-door" style="height:83px" role="img" aria-label="Sliding door photo"></div><p>Door Hardware</p></div>
      <div class="tile" style="left:163px;top:707px"><div class="thumb g-fence" style="height:84px" role="img" aria-label="Pool fence photo"></div><p>Fenching &amp; Gates</p></div>
      <div class="tile" style="left:163px;top:840px"><div class="thumb g-timber" style="height:86px" role="img" aria-label="Timber block photo"></div><p>Timber</p></div>
      <nav class="tabbar">
        <a class="tab"><svg class="ic"><use href="#i-home"/></svg><span>Home</span></a>
        <a class="tab active"><svg class="ic"><use href="#i-search"/></svg><span>Browse</span></a>
        <a class="tab"><svg class="ic"><use href="#i-cart"/></svg><span>Basket</span></a>
        <a class="tab"><svg class="ic"><use href="#i-gear"/></svg><span>Setting</span></a>
      </nav>
    </section>
  </div>

  <div class="slot" style="left:1338px;top:808px">
    <section class="phone" style="height:692px">
      <div class="status"><span>9:41</span><svg><use href="#i-status"/></svg></div>
      <svg class="ic back"><use href="#i-left"/></svg>
      <h1 class="title">Live Tracking</h1>
      <svg class="ic cart-top"><use href="#i-cart"/></svg><i class="badge" style="left:252px;top:44px">1</i>
      <svg class="ic kebab"><use href="#i-kebab"/></svg>
      <p class="eta">In 15 min</p>
      <p class="eta-sub">Estimated arrival time: <b>6.00 pm</b></p>
      <div class="map" role="img" aria-label="Street map with the delivery route from store to site"></div>
      <div class="plate"><span class="dot"></span><span><small>Scooty</small><strong>BAC-XXXX</strong></span></div>
      <div class="driver">
        <div class="avatar" style="left:10px;top:17px;width:36px;height:36px" role="img" aria-label="Driver photo"></div>
        <div class="who">Driver Name<strong>Sam Ortega</strong><em><b>★</b> 4.5</em></div>
        <span class="profile-link">View Profile <svg class="ic"><use href="#i-right"/></svg></span>
      </div>
      <div class="message"><span>Send a message...</span><svg class="ic"><use href="#i-mic"/></svg></div>
      <div class="call"><svg><use href="#i-phone"/></svg></div>
    </section>
  </div>

  <p class="signature brand">Kit Runner</p>
</main>
</body>
</html>
```